Quorvalant Business card

we are a cloud data network and voice business communication's company - we target small and medium size business - please look into our website to learn more quorvalant-example.com
Target Market(s)
small business and mid size
Logo Text
QUORVALANT
Logo styles of interest
Abstract Logo
Lettermark Logo
Requirements
Must have
- LOGO, SLOGAN ( together we connect the world ) name title email, fax, our colors are grey white back and blue - on the back we want to have 4 icon logos a phone, a cloud , data, network

```html
<!DOCTYPE html>
<html lang="en">
<head>
<meta charset="utf-8">
<title>Quorvalant Business Card</title>
<link rel="stylesheet" href="https://fonts.googleapis.com/css2?family=Oswald:wght@700&family=Cabin:wght@400&family=Arimo:wght@400;700&display=swap">
<style>
  :root {
    --brand-blue: #1b3a8a;
    --icon-blue: #0b72b9;
    --brand-grey: #888888;
    --panel-grey: #727170;
    --ink: #222222;
    --tagline-grey: #9a9a9a;
    --white: #ffffff;
  }
  * { margin: 0; padding: 0; box-sizing: border-box; }
  html, body { width: 1200px; height: 1000px; overflow: hidden; background: var(--white); }
  .canvas { position: relative; width: 1200px; height: 1000px; }

  .brand-mark { position: absolute; background: var(--brand-blue); border-radius: 14%; }
  .wordmark {
    position: absolute; font-family: "Oswald", sans-serif; font-weight: 700;
    color: var(--brand-blue); line-height: 1; white-space: nowrap;
  }
  .tagline {
    position: absolute; font-family: "Cabin", sans-serif; font-weight: 400;
    line-height: 1; white-space: nowrap;
  }

  .hero-mark { left: 549px; top: 123px; width: 129px; height: 124px; }
  .hero-wordmark { left: 383px; top: 268px; width: 466px; text-align: center; font-size: 84px; letter-spacing: 1px; }
  .hero-tagline { left: 383px; top: 353px; width: 466px; text-align: center; font-size: 32px; color: var(--ink); }

  .presentation { position: absolute; left: 31px; top: 515px; width: 1154px; height: 450px; background: var(--panel-grey); }
  .side-label {
    position: absolute; top: 571px; width: 200px; text-align: center;
    font-family: "Arimo", sans-serif; font-size: 24px; color: var(--white);
  }
  .side-label.front { left: 190px; }
  .side-label.back { left: 792px; }

  .card {
    position: absolute; top: 628px; width: 493px; height: 295px; background: var(--white);
    overflow: hidden; box-shadow: 0 6px 22px rgba(0,0,0,0.45);
  }
  .card-front { left: 99px; }
  .card-back { left: 656px; }

  .front-mark { left: 357px; top: 27px; width: 50px; height: 48px; }
  .front-wordmark { left: 292px; top: 81px; width: 182px; text-align: center; font-size: 32px; }
  .front-tagline { left: 292px; top: 117px; width: 182px; text-align: center; font-size: 12.5px; color: var(--ink); }
  .holder {
    position: absolute; left: 33px; top: 142px;
    font-family: "Arimo", sans-serif; font-size: 16.5px; line-height: 20px; color: var(--ink);
  }
  .website {
    position: absolute; left: 291px; top: 255px;
    font-family: "Arimo", sans-serif; font-weight: 700; font-size: 12.5px; letter-spacing: 1.6px; color: var(--ink);
  }

  .back-wordmark { left: 32px; top: 35px; font-size: 20px; }
  .contact {
    position: absolute; left: 32px; top: 71px;
    font-family: "Arimo", sans-serif; font-size: 13.5px; line-height: 16.5px; color: var(--ink);
  }
  .back-tagline { left: 32px; top: 141px; font-size: 21px; color: var(--tagline-grey); }
  .service-band {
    position: absolute; left: 0; top: 174px; width: 493px; height: 121px; background: var(--brand-blue);
  }
  .service-icons { position: absolute; left: 0; top: 0; }
</style>
</head>
<body>
<main class="canvas">
  <section class="logo-lockup">
    <div class="brand-mark hero-mark"></div>
    <div class="wordmark hero-wordmark">QUORVALANT</div>
    <div class="tagline hero-tagline">together we connect the world</div>
  </section>

  <section class="presentation"></section>
  <div class="side-label front">FRONT</div>
  <div class="side-label back">BACK</div>

  <article class="card card-front">
    <div class="brand-mark front-mark"></div>
    <div class="wordmark front-wordmark">QUORVALANT</div>
    <div class="tagline front-tagline">together we connect the world</div>
    <div class="holder">NAME<br>Designation</div>
    <div class="website">www.quorvalant-example.com</div>
  </article>

  <article class="card card-back">
    <div class="wordmark back-wordmark">QUORVALANT</div>
    <div class="contact">
      555.014.2290 and 800.555.0147<br>
      418 N Harbor Ave<br>
      Lakemont FL 30917
    </div>
    <div class="tagline back-tagline">together we connect the world</div>
    <div class="service-band">
      <svg class="service-icons" width="493" height="121" viewBox="0 0 493 121" aria-label="Phone, cloud, network and mail icons">
        <g fill="var(--icon-blue)" stroke="none">
          <!-- phone handset -->
          <path d="M52 14 l10 5 -9 22 -8 -3 c-6 12 -8 26 -7 40 l8 -1 -2 24 -11 -1 c-8 -26 -4 -62 19 -86z"/>
          <!-- cloud -->
          <path d="M104 97 h100 a22 22 0 0 0 0 -44 a22 22 0 0 0 -22 -6 a30 30 0 0 0 -56 8 a20 20 0 0 0 -22 20 a21 21 0 0 0 0 22z"/>
          <!-- wireless network -->
          <circle cx="302" cy="87" r="8"/>
        </g>
        <g fill="none" stroke="var(--icon-blue)" stroke-width="7" stroke-linecap="round">
          <path d="M284 73 a26 26 0 0 1 36 0"/>
          <path d="M272 60 a42 42 0 0 1 60 0"/>
          <path d="M266 46 a52 52 0 0 0 0 0"/>
        </g>
        <g fill="none" stroke="var(--icon-blue)" stroke-width="3" stroke-linejoin="round">
          <!-- document -->
          <path d="M430 26 h22 l16 16 v42 h-38z"/>
          <path d="M452 26 v16 h16"/>
          <path d="M437 50 h12 M437 56 h20 M437 62 h20"/>
          <!-- envelope -->
          <path d="M375 52 h72 v44 h-72z" fill="var(--brand-blue)"/>
          <path d="M375 52 l36 26 36 -26 M375 96 l26 -20 M447 96 l-26 -20"/>
        </g>
      </svg>
    </div>
  </article>
</main>
</body>
</html>
```